fizzy drinks label design

I want to design fizzy drink label for 3 flavors : black grapes, red apple and mojito, band name kestrola, product name KOLTA , product will be in plastic bottle, label size 198 mm X 66mm

```html
<!DOCTYPE html>
<html lang="en">
<head>
<meta charset="utf-8">
<title>Kestrola KOLTA – Fizzy Drink Labels</title>
<link rel="stylesheet" href="https://fonts.googleapis.com/css2?family=Archivo+Black&family=Russo+One&family=Saira+Condensed:wght@600;700&family=Roboto:wght@400&display=swap">
<style>
  :root {
    --apple: #c30d1b;
    --grape: #3d0d4a;
    --mojito: #5ab31e;
    --badge: #11d4f7;
    --ink: #111111;
    --paper: #ffffff;
    --splash-soft: #d8e8fb;
  }
  * { box-sizing: border-box; margin: 0; padding: 0; }
  html, body { width: 1200px; height: 1200px; overflow: hidden; background: var(--paper); }
  .canvas { position: relative; width: 1200px; height: 1200px; background: var(--paper); }

  .label {
    position: absolute;
    top: 109px;
    width: 330px;
    height: 989px;
    border: 27px solid var(--flavor);
    border-radius: 34px;
    background: var(--paper);
    overflow: hidden;
  }
  .label--apple { left: 80px; --flavor: var(--apple); }
  .label--grape { left: 432px; --flavor: var(--grape); }
  .label--mojito { left: 785px; --flavor: var(--mojito); }

  .brand {
    position: absolute;
    top: 12px; left: 0; right: 0;
    text-align: center;
    font-family: "Saira Condensed", sans-serif;
    font-weight: 700;
    font-size: 27px;
    letter-spacing: 0.5px;
    color: var(--ink);
    line-height: 1;
  }

  .category {
    position: absolute;
    top: 68px; left: 50%;
    transform: translateX(-50%);
    background: var(--badge);
    color: var(--paper);
    font-family: "Saira Condensed", sans-serif;
    font-weight: 600;
    font-size: 20px;
    line-height: 26px;
    padding: 0 7px;
    border-radius: 4px;
    white-space: nowrap;
  }

  .product-name {
    position: absolute;
    top: 128px; left: 0; right: 0;
    display: flex;
    flex-direction: column;
    align-items: center;
    font-family: "Russo One", sans-serif;
    font-weight: 400;
    font-size: 86px;
    line-height: 75px;
    color: var(--flavor);
    text-shadow: 3px 3px 2px rgba(0,0,0,0.25);
  }
  .product-name span { display: block; }
  .product-name span:nth-child(1) { transform: rotate(12deg); }
  .product-name span:nth-child(2) { transform: rotate(-10deg) translateX(4px); }
  .product-name span:nth-child(4) { transform: rotate(6deg); }
  .product-name span:nth-child(5) { transform: rotate(-12deg); }

  .splash {
    position: absolute;
    top: 380px; left: 0; right: 0; height: 520px;
    background: radial-gradient(ellipse 60% 45% at 50% 55%, var(--splash-soft) 0%, rgba(216,232,251,0.5) 55%, rgba(255,255,255,0) 80%);
  }

  .hero {
    position: absolute;
    top: 530px; left: 22px; right: 22px; height: 262px;
    border-radius: 46% 46% 40% 40%;
  }
  .hero--apple { background: radial-gradient(circle at 45% 55%, #e02a2a 0%, #b30f16 60%, #8a1016 100%); }
  .hero--grape { background: radial-gradient(circle at 50% 55%, #4a4a50 0%, #242428 60%, #111 100%); }
  .hero--mojito { background: radial-gradient(circle at 50% 55%, #dff7e0 0%, #a6e39f 55%, #6fc35d 100%); }

  .flavor {
    position: absolute;
    left: 0; right: 0;
    bottom: 28px;
    text-align: center;
    font-family: "Archivo Black", sans-serif;
    color: var(--flavor);
    font-size: 31px;
    line-height: 32px;
    text-shadow: 2px 2px 2px rgba(0,0,0,0.25);
  }
  .flavor-word { display: block; }
  .flavor-tag {
    display: block;
    font-family: "Roboto", sans-serif;
    font-size: 13px;
    line-height: 14px;
    color: var(--ink);
    text-shadow: none;
  }
</style>
</head>
<body>
<main class="canvas">

  <section class="label label--apple">
    <div class="brand">kestrola</div>
    <div class="category">FIZZY DRINKS</div>
    <div class="splash"></div>
    <h1 class="product-name" aria-label="KOLTA"><span>K</span><span>O</span><span>L</span><span>T</span><span>A</span></h1>
    <div class="hero hero--apple" role="img" aria-label="Two red apples with leaves in a water splash"></div>
    <p class="flavor"><span class="flavor-word">RED</span><span class="flavor-word">APPLE</span><span class="flavor-tag">FLAVOR</span></p>
  </section>

  <section class="label label--grape">
    <div class="brand">kestrola</div>
    <div class="category">FIZZY DRINKS</div>
    <div class="splash"></div>
    <h1 class="product-name" aria-label="KOLTA"><span>K</span><span>O</span><span>L</span><span>T</span><span>A</span></h1>
    <div class="hero hero--grape" role="img" aria-label="Bunch of black grapes with vine leaves in a water splash"></div>
    <p class="flavor"><span class="flavor-word">BLACK</span><span class="flavor-word">GRAPES</span><span class="flavor-tag">FLAVOR</span></p>
  </section>

  <section class="label label--mojito">
    <div class="brand">kestrola</div>
    <div class="category">FIZZY DRINKS</div>
    <div class="splash"></div>
    <h1 class="product-name" aria-label="KOLTA"><span>K</span><span>O</span><span>L</span><span>T</span><span>A</span></h1>
    <div class="hero hero--mojito" role="img" aria-label="Two glasses of mojito with lime slices, mint and ice"></div>
    <p class="flavor"><span class="flavor-word">MOJITO</span><span class="flavor-tag">FLAVOR</span></p>
  </section>

</main>
</body>
</html>
```